I'm looking for an edgy and contemporary book cover rebranding

I have nearly completed a revised edition of my book 'GRIEF AWAY NOW" that was published in 2019. The book helped readers struggling with the shame associated with their mental health challenges.

Several of my readers encouraged me to adapt the book to younger readers - teenagers. I am now in the process of rewriting my book for teenage readers: 'GRIEF AWAY NOW - FOR TEENAGERS.'

Ideally the book cover should look similar, yet with a 'youth edge' to the design.

Grief Away Now 4 teens or for teens

Grief Away Now 4 teenagers or for teenagers.

Please keep the photo but make in more abstract - see attached example (Rise-higher with Tobin Vael).

Target Market(s)

Teenagers and possibly parents of teenagers

Industry/Entity Type

Mental health and wellbeing

Font styles to use
Sans Serif

Colors

Designer to choose colors to be used in the design.

Requirements
Must have
• There is a connection to the first edition of my book and appeals to young readers
Nice to have
• Contemporary and youthful design that connects with the first edition.
Should not have
• Cover looks childish or feminine

```html
<!DOCTYPE html>
<html lang="en">
<head>
<meta charset="utf-8">
<title>Grief Away Now – For Teenagers – Book Cover Wrap</title>
<link href="https://fonts.googleapis.com/css2?family=Nunito+Sans:wght@400;600&family=Montserrat:wght@500;600&family=Alfa+Slab+One&display=swap" rel="stylesheet">
<style>
  :root {
    --ink: #05070a;
    --night: #0b1018;
    --white: #ffffff;
    --text: #e6e9ee;
    --accent-blue: #1d7fc4;
    --stamp-red: #d9202a;
    --rule: #1f6fb0;
    --brand: #8fa3c8;
  }
  * { margin: 0; padding: 0; box-sizing: border-box; }
  html, body { width: 1200px; height: 881px; overflow: hidden; background: var(--ink); }
  .wrap { position: relative; width: 1200px; height: 881px; background: var(--ink); overflow: hidden;
    font-family: "Nunito Sans", sans-serif; color: var(--text); }

  .cover-photo { position: absolute; left: 540px; top: 0; width: 660px; height: 881px;
    background:
      radial-gradient(ellipse 170px 220px at 360px 300px, rgba(138,106,85,.85), rgba(138,106,85,0) 75%),
      radial-gradient(ellipse 320px 360px at 300px 280px, rgba(111,134,176,.55), rgba(111,134,176,0) 70%),
      radial-gradient(ellipse 380px 420px at 440px 650px, rgba(40,48,62,.9), rgba(11,16,24,0) 75%),
      var(--ink); }

  /* back cover */
  .blurb { position: absolute; left: 64px; top: 50px; width: 472px; font-size: 14px; line-height: 20.3px; }
  .blurb p { margin-bottom: 12.3px; }
  .back-rule { position: absolute; left: 64px; top: 571px; width: 473px; height: 1px; background: var(--rule); }
  .author-photo { position: absolute; left: 64px; top: 596px; width: 181px; height: 176px;
    background: linear-gradient(180deg, #5a6577 0%, #c99a76 45%, #4b6f86 70%, #1c2530 100%); }
  .author-url { position: absolute; left: 64px; top: 778px; width: 181px; text-align: center; font-size: 13px; letter-spacing: .5px; }
  .author-bio { position: absolute; left: 266px; top: 600px; width: 274px; font-size: 13px; line-height: 17.5px; }
  .brand { position: absolute; display: flex; align-items: center; gap: 6px;
    font-weight: 600; color: var(--brand); white-space: nowrap; }
  .brand .dot { display: inline-block; background: var(--brand); }
  .brand-back { left: 258px; top: 808px; font-size: 16px; }
  .brand-back .dot { width: 12px; height: 12px; }
  .brand-spine { left: 578px; top: 820px; font-size: 9px; }
  .brand-spine .dot { width: 7px; height: 7px; }

  /* spine */
  .spine-text { position: absolute; writing-mode: vertical-rl; white-space: nowrap; }
  .spine-author { left: 592px; top: 54px; font-family: "Montserrat", sans-serif; font-weight: 500; font-size: 19px; letter-spacing: 5px; color: #c9d3e2; }
  .spine-title { left: 588px; top: 292px; font-family: "Montserrat", sans-serif; font-weight: 500; font-size: 30px; letter-spacing: .5px; color: var(--white); }
  .spine-sub { left: 598px; top: 648px; font-family: "Alfa Slab One", serif; font-size: 12px; letter-spacing: .5px; color: var(--stamp-red); }

  /* front */
  .front-author { position: absolute; left: 762px; top: 44px; font-family: "Montserrat", sans-serif; font-weight: 600;
    font-size: 37px; letter-spacing: 9px; color: var(--white); white-space: nowrap; }
  .front-type { position: absolute; left: 600px; top: 0; width: 600px; height: 881px; }
  .title-line { font-family: "Montserrat", sans-serif; font-weight: 600; fill: var(--white); }
  .subtitle { font-family: "Montserrat", sans-serif; font-weight: 600; font-size: 18px; fill: var(--accent-blue); }
  .stamp-frame { fill: none; stroke: var(--stamp-red); stroke-width: 4; }
  .stamp-text { font-family: "Alfa Slab One", serif; font-size: 30px; fill: var(--stamp-red); }
</style>
</head>
<body>
<div class="wrap">
  <div class="cover-photo" role="img" aria-label="Abstract portrait of the author dissolving into scattered dark particles against a dark blue background"></div>

  <section class="back-cover">
    <div class="blurb">
      <p>Do you have an irritating feeling inside? Is there something mysterious hindering you, pulling you down, and holding you back?</p>
      <p>Shame is an intimidating sense of inferiority, which could be causing you to feel the way you do.</p>
      <p>GRIEF AWAY NOW focuses on the shame connected with mental health struggles. It will take you on a pilgrimage for your soul, embracing the ancient wisdom of the Biblical narrative of shame and grace.</p>
      <p>Underlying this ancient and timeless wisdom is a down-to-earth biography of Dan Keller’s journey of steadfast faith in God while navigating through the turmoil of shame, chronic anxiety, and panic attacks. Be assured that this book is readable, relatable, and profoundly practical.</p>
      <p>Each chapter offers a fresh and insightful perspective on the nature of shame and the collateral damage it causes. You will gain invaluable knowledge of the catastrophic birth of shame, shame triggers, and the destructive shame narrative.</p>
      <p>Don’t settle for concealing, distracting, and numbing your shame. There is no magical formula of recovery or a one-size-fits-all solution. The way out of shame is a daring journey that encompasses courageous vulnerability and dramatic ebbs and flows.</p>
      <p>Are you ready to be a shame buster? Start reading and start moving in partnership with the Holy Spirit into shame-free living.</p>
    </div>
    <div class="back-rule"></div>
    <div class="author-photo" role="img" aria-label="Portrait photo of the author at the seaside at sunset"></div>
    <div class="author-url">www.dankeller.co</div>
    <p class="author-bio">Dan Keller is a mental health advocate, expressing his passion through speaking, writing, and mentoring. Dan and his wife Laura were the lead pastors of a Harbor Church in Fremont, Lakeshore County, for twenty-three years. They have two adult children, Mia and Owen.</p>
    <div class="brand brand-back"><span class="dot"></span>dan keller</div>
  </section>

  <section class="spine">
    <div class="spine-text spine-author">DAN KELLER</div>
    <div class="spine-text spine-title">GRIEF AWAY NOW</div>
    <div class="spine-text spine-sub">FOR TEENAGERS</div>
    <div class="brand brand-spine"><span class="dot"></span>dan keller</div>
  </section>

  <section class="front-cover">
    <div class="front-author">DAN KELLER</div>
    <svg class="front-type" viewBox="0 0 600 881" width="600" height="881" aria-label="GRIEF AWAY NOW – For Teenagers – Unshaming mental health struggles">
      <text class="title-line" x="76" y="698" font-size="136" textLength="476" lengthAdjust="spacingAndGlyphs">GRIEF</text>
      <text class="title-line" x="76" y="800" font-size="108" textLength="476" lengthAdjust="spacingAndGlyphs">AWAY NOW</text>
      <g class="stamp" transform="rotate(-8 435 568)">
        <rect class="stamp-frame" x="290" y="545" width="290" height="46"/>
        <text class="stamp-text" x="302" y="580" textLength="266" lengthAdjust="spacingAndGlyphs">FOR TEENAGERS</text>
      </g>
      <text class="subtitle" x="76" y="832" textLength="476" lengthAdjust="spacing">UNSHAMING MENTAL HEALTH STRUGGLES</text>
    </svg>
  </section>
</div>
</body>
</html>
```